GlowRY (Beer/Wine candles) Edgy Candle with a Cause

Help us to help others. GlowRy is a beautifully scented natural soy candle made using repurposed beer/ wine bottles while at the same time donating a portion of our profits to youth alcohol education programs. (1. Waste = Repurposed beer/wine bottle, 2.) GlowRy = (anti) drunk/alcohol 3.) Ed = education/prevention programs.)
We're looking for a design that is cool and bold yet elegant and appeals to women (90% of our customers.) No traditional beer label designs please.

The "GlowRY" logo should appear prominently in the design with the scent name (in a different font) "on top." (See the "Chocolate Glowry" poster attached.

Examples of actual scents: Maple Drift, Dancing Daiquiri, Fizzy Mock-tail. (None of the fragrances smell like beer/alcohol or wine.)

Also the ED in GlowRRY should stand out in some way.

The emphasis should not be on the recycling aspect, so no obvious recycling symbols.

We are open to different interpretations and have attached varying examples that we like.
Note: a "blackboard/chalkboard" label is an idea since this deals with education.

Note: files & fonts used in the final design should be editable so that we can add other scent names as needed.

Target Market(s)

Candle buyers, specifically women between the ages of 16-45

Requirements
Must have
• 1.)Free fonts or license fonts under $20.00 2.) fonts modified to look unique/original. 3.) Editable Scent name 4.) Burning instructions 5.) Warning Info
• Burning Instructions: Trim wick to 1/4" before each lighting. Keep free from foreign materials including wick trimmings. For an even burn, burn for at least 1 hour but not more than 4 hours at a time. Discontinue use when 1/4" of wax remains. Discard or recycle after use.
• Warning: Burn candle within sight. Keep out of reach of children and pets. Keep away from things that catch fire. Use with caution.
Nice to have
• Colored Scent Names
Should not have
• recycle symbols

```html
<!DOCTYPE html>
<html lang="en">
<head>
<meta charset="utf-8">
<title>GlowRY Soy Candle Label</title>
<link href="https://fonts.googleapis.com/css2?family=Caveat:wght@400;500&family=Caveat+Brush&family=Cabin+Sketch:wght@700&family=Mr+Dafoe&family=Architects+Daughter&display=swap" rel="stylesheet">
<style>
  :root {
    --page: #ffffff;
    --board: #38393d;
    --board-deep: #2e2f33;
    --chalk: #f2f2ee;
    --chalk-soft: #dcdcd6;
    --pink: #f0506e;
    --badge-red: #e8333c;
  }
  * { margin: 0; padding: 0; box-sizing: border-box; }
  html, body {
    width: 1200px; height: 773px; overflow: hidden;
    background: var(--page);
  }
  .canvas { position: relative; width: 1200px; height: 773px; }
  .label {
    position: absolute; left: 60px; top: 203px; width: 1088px; height: 362px;
    background: radial-gradient(ellipse at 40% 45%, var(--board) 0%, var(--board-deep) 100%);
    color: var(--chalk);
    overflow: hidden;
  }
  .label > * { position: absolute; }

  .scent-name {
    left: 120px; top: 18px; width: 370px; text-align: center;
    font-family: "Mr Dafoe", cursive; font-size: 48px; line-height: 1;
    white-space: nowrap;
    color: var(--pink);
  }
  .brand-name {
    left: 118px; top: 98px; width: 356px; text-align: center;
    font-family: "Cabin Sketch", sans-serif; font-weight: 700;
    font-size: 80px; line-height: 1; letter-spacing: 1px;
    white-space: nowrap;
    color: var(--chalk);
  }
  .product-type {
    left: 215px; top: 186px; width: 175px; text-align: center;
    font-family: "Architects Daughter", sans-serif; font-size: 30px; line-height: 1.2;
    border-bottom: 2px solid var(--chalk);
    padding-bottom: 2px;
  }
  .hand-poured {
    left: 8px; top: 162px;
    font-family: "Architects Daughter", sans-serif; font-size: 19px; line-height: 1.25;
    transform: rotate(8deg);
  }
  .hand-poured span { display: block; }
  .hand-poured span:last-child { padding-left: 18px; transform: rotate(-14deg); }
  .cause {
    left: 88px; top: 254px; width: 380px;
    font-family: "Caveat Brush", cursive; font-size: 25px; line-height: 1.35;
    white-space: nowrap;
    transform: rotate(-2deg);
  }
  .cause span { display: block; }
  .cause span:last-child { padding-left: 67px; }
  .net-weight {
    left: 277px; top: 336px;
    font-family: "Architects Daughter", sans-serif; font-size: 16px; line-height: 1;
  }
  .burn-time-icon { left: 513px; top: 118px; width: 44px; height: 40px; }
  .burn-time {
    left: 520px; top: 148px;
    font-family: "Architects Daughter", sans-serif; font-size: 19px; line-height: 1.15;
  }
  .burn-time span { display: block; transform: rotate(14deg); }
  .burn-time span:nth-child(1) { padding-left: 14px; }
  .burn-time span:nth-child(3) { padding-left: 24px; }
  .age-badge { left: 503px; top: 278px; width: 64px; height: 64px; }

  .instructions, .warning {
    font-family: "Caveat", cursive; font-weight: 400; color: var(--chalk);
  }
  .instructions {
    left: 594px; top: 20px; width: 414px;
    font-size: 19px; line-height: 21px; letter-spacing: -0.3px;
  }
  .warning {
    left: 659px; top: 274px; width: 392px;
    font-size: 21px; line-height: 25px; letter-spacing: -0.2px;
  }
  .instructions strong, .warning strong {
    font-weight: 500; text-decoration: underline; text-underline-offset: 3px;
  }
  .timer-art {
    left: 1021px; top: 20px; width: 52px; height: 52px; border-radius: 50%;
    background: radial-gradient(circle, #56575c 0%, #45464b 100%);
    border: 2px solid var(--chalk-soft);
  }
  .safety-art {
    left: 690px; top: 140px; width: 325px; height: 118px; border-radius: 10px;
    background: linear-gradient(90deg, #46474c 0%, #4e4f54 50%, #46474c 100%);
  }
  .chalk-arrows { left: 0; top: 0; width: 1088px; height: 362px; pointer-events: none; }
</style>
</head>
<body>
<div class="canvas">
  <section class="label">
    <p class="scent-name">Dancing Daiquiri</p>
    <h1 class="brand-name">GlowRY</h1>
    <p class="product-type">Soy Candle</p>
    <p class="hand-poured"><span>HAND-</span><span>POURED</span></p>
    <p class="cause"><span>Donating a portion of profits to</span><span>youth alcohol education programs</span></p>
    <p class="net-weight">100 G</p>

    <svg class="burn-time-icon" viewBox="0 0 44 40" aria-hidden="true">
      <path d="M6 36 C2 26 10 20 12 10 C16 18 18 20 20 14 C24 22 26 6 30 2 C32 14 40 20 36 36"
            fill="none" stroke="var(--chalk)" stroke-width="2" stroke-linecap="round"/>
    </svg>
    <p class="burn-time"><span>48HR</span><span>BURN</span><span>TIME</span></p>

    <svg class="age-badge" viewBox="0 0 64 64" role="img" aria-label="Adults only notice">
      <circle cx="32" cy="32" r="28" fill="none" stroke="var(--badge-red)" stroke-width="4"/>
      <line x1="52" y1="12" x2="12" y2="52" stroke="var(--badge-red)" stroke-width="4"/>
    </svg>

    <p class="instructions"><strong>Burning Instructions:</strong> Trim wick to 1/4" before each lighting. Keep free from foreign materials including wick trimmings. For an even burn, burn for at least 1 hour but not more than 4 hours at a time. Discontinue use when 1/4" of wax remains. Discard or recycle after use.</p>

    <div class="timer-art" role="img" aria-label="Chalk drawing of a clock"></div>
    <div class="safety-art" role="img" aria-label="Chalk drawing of a cat and a child reaching toward a lit candle"></div>

    <p class="warning"><strong>Warning:</strong> Burn candle within sight. Keep out of reach of children and pets. Keep away from things that catch fire. Use with caution.</p>

    <svg class="chalk-arrows" viewBox="0 0 1088 362" aria-hidden="true">
      <g fill="none" stroke="var(--chalk)" stroke-width="2" stroke-linecap="round">
        <path d="M958 122 C990 120 1005 112 1020 100"/>
        <path d="M1008 100 L1020 100 L1014 110"/>
        <path d="M636 300 C620 260 625 225 682 204"/>
        <path d="M670 200 L683 204 L674 214"/>
      </g>
    </svg>
  </section>
</div>
</body>
</html>
```